Etiketten
Zielgruppe
Wir produzieren Nudeln.
Zielgruppe sind Einheimische und Touristen, 1.die den Unterschied zur Industrieware schätzen und gute Produkte sich selbst gönnen
2. die ein Geschenk oder Genuss aus dem Allgäu mitnehmen möchten
Aufgabenstellung
Produktetikett für Nudeln.
Es soll den Kunden davon überzeugen, genau dieses Nudelpaket aus dem Regal zu kaufen. Es soll suggerieren dass es sich um sehr gute Qualität handelt die man schmeckt.
Es soll im Regal auffallen um sich die Nudeln auch als Geschenk mitzunehmen.
Es soll die Region Allgäu, Westallgäu mit Adelegg wiederspiegeln.
Die Abmessung beträgt Breite 10cm Höhe 12cm, jeweils plus 3mm Beschnittzugabe für die Druckerei.
Es gibt nur eine Vorderseite.
Es soll nicht verspielt wirken. Gern mit Witz.
Slogan zum Beispiel: Kessners Teigla-orginal Allgäuer Pasta. Hier kann gern auch ein anderer passender Slogan verwendet werden.
Das Etikett sollte auf verschiedene Themenbereiche anwendbar sein, da wir unterschiedliche Nudelsorten produzieren.
Verkaufsorte sind kleine Dorfläden, Laden in Manufaktur, wo auch andere Erzeuger ihre selbstgemachten Produkte für Einheimische und Touristen anbieten. Lebensmittelautomaten und Direktverkauf.

```html
<!DOCTYPE html>
<html lang="de">
<head>
<meta charset="utf-8">
<title>Kessners Teigla – Etikett</title>
<link rel="stylesheet" href="https://fonts.googleapis.com/css2?family=Playwrite+DE+VA&family=Source+Sans+3:wght@300&display=swap">
<style>
  :root {
    --canvas-bg: #ffffff;
    --label-bg: #cbc8b6;
    --ink: #111111;
    --symbol-fill: #3a3a3a;
    --sub-ink: #222222;
  }
  html, body {
    margin: 0;
    padding: 0;
    width: 745px;
    height: 1200px;
    overflow: hidden;
    background: var(--canvas-bg);
  }
  .canvas {
    position: relative;
    width: 745px;
    height: 1200px;
  }
  .label {
    position: absolute;
    left: 50px;
    top: 213px;
    width: 645px;
    height: 774px;
    background: var(--label-bg);
  }
  .brand-name {
    position: absolute;
    right: 78px;
    top: 70px;
    margin: 0;
    font-family: "Playwrite DE VA", cursive;
    font-weight: 400;
    font-size: 44px;
    line-height: 80px;
    color: var(--ink);
    white-space: nowrap;
    text-align: right;
  }
  .product-symbol {
    position: absolute;
    left: 346px;
    top: 214px;
    width: 205px;
    height: 250px;
    background: var(--symbol-fill);
    opacity: 0.85;
  }
  .tagline {
    position: absolute;
    right: 97px;
    top: 480px;
    margin: 0;
    text-align: right;
    font-family: "Source Sans 3", sans-serif;
    font-weight: 300;
    font-size: 40px;
    line-height: 57px;
    color: var(--sub-ink);
  }
  .motto {
    position: absolute;
    right: 97px;
    top: 664px;
    margin: 0;
    font-family: "Playwrite DE VA", cursive;
    font-size: 28px;
    line-height: 54px;
    color: var(--ink);
    white-space: nowrap;
    -webkit-text-stroke: 0.9px var(--ink);
  }
</style>
</head>
<body>
<main class="canvas">
  <section class="label">
    <h1 class="brand-name">Kessners Teigla</h1>
    <div class="product-symbol" role="img" aria-label="Bildzeichen: sechs senkrechte gewellte Nudeln"></div>
    <p class="tagline">Orginal<br>Allgäuer<br>Pasta</p>
    <p class="motto">'s ischt halt so</p>
  </section>
</main>
</body>
</html>
```